Corporate Identity & Brand book of k7

k7 is a service platform around events, prints, gadgets and booth-building.
We deliver service only for B2B with a very high quality standard, service-level, professionalism, affordable price for tailor-made solutions.

We developped last year a new (very good!) logo 'k7' and a tagline 'Beyond Expectations'.

Our colors are black, white and sand...

BUT...

We do not have any extra branding guidelines, elements, touches to get a real identity. From the moment we want to make a business card, invoice, brochure, car wrap, etc, we do not have any 'corporate identity' to develop it correctly and the identify us to our clients.

Our logo is great, the black and white colors are great, but the sandy color is too soft (no identification to our company). We are looking for something more to make it alive and to creat a full brand book and basic documents to create :

• Corporate identity
• Brand book
• Presentation brochures
• Business cards
• Car wrapping
• Newsletter
• Promotionnal bags
• E-mail signature
• Boxes for shipment
• Panel on our office
• Flags
• Presentation maps
• Shipment tape
• Rollup
• Powerpoint branding
• Lanyards
• Invoices templates
• Offers templates

So, we are asking for this request to make the brand book and to integrate the listed items.

And our black and white colors are not enough to make it attractive. We think that a nobel/rich color could fit with our image (like coper, bronze, or the color attached).

You can have a look to our temporary website ([url removed, login to view]) to better understand our work, service and philosophy.

```html
<!DOCTYPE html>
<html lang="en">
<head>
<meta charset="utf-8">
<title>k7 — Stationery Identity</title>
<link rel="stylesheet" href="https://fonts.googleapis.com/css2?family=Open+Sans:wght@400;600;700&display=swap">
<style>
  :root {
    --backdrop: #2b2b2c;
    --paper-black: #1b1b1c;
    --paper-black-edge: #242425;
    --paper-white: #efefee;
    --copper: #c27d5e;
    --copper-deep: #9a5b40;
    --watermark: #e2e2e1;
    --ink-grey: #8a8a8a;
  }
  * { box-sizing: border-box; margin: 0; padding: 0; }
  html, body { width: 1200px; height: 800px; overflow: hidden; }
  body {
    background: var(--backdrop);
    font-family: "Open Sans", Arial, sans-serif;
    position: relative;
  }
  .sheet { position: absolute; box-shadow: 0 14px 30px rgba(0,0,0,.45); }

  .brand-name { color: var(--copper); font-weight: 700; letter-spacing: -1px; line-height: 1; }
  .tagline { color: var(--copper); font-size: 9px; margin-top: 3px; font-weight: 400; }

  /* Letterhead */
  .letterhead {
    left: 40px; top: 90px; width: 320px; height: 452px;
    background: var(--paper-white);
  }
  .letterhead .brand { position: absolute; top: 26px; left: 0; right: 0; text-align: center; }
  .letterhead .brand-name { font-size: 30px; }
  .letterhead .watermark {
    position: absolute; top: 120px; left: 0; right: 0; text-align: center;
  }
  .watermark .brand-name { color: var(--watermark); font-size: 96px; }
  .watermark .tagline { color: var(--watermark); font-size: 20px; font-weight: 700; }
  .contact { position: absolute; left: 24px; bottom: 96px; font-size: 8px; color: var(--ink-grey); line-height: 1.9; }
  .contact span { color: var(--copper); display: inline-block; width: 12px; }

  .rules { position: absolute; display: flex; flex-direction: column; align-items: flex-end; gap: 9px; }
  .rules i { display: block; height: 1.5px; background: linear-gradient(90deg, var(--copper-deep), var(--copper)); }
  .letterhead .rules { right: 24px; bottom: 36px; }

  /* Folder */
  .folder {
    left: 390px; top: 40px; width: 420px; height: 560px;
    background: var(--paper-black); border: 1px solid var(--paper-black-edge);
  }
  .folder .brand { position: absolute; top: 150px; left: 0; right: 0; text-align: center; }
  .folder .brand-name { font-size: 72px; }
  .folder .tagline { font-size: 17px; margin-top: 6px; }
  .folder .rules { right: 36px; bottom: 50px; gap: 12px; }

  /* Business card */
  .business-card {
    left: 840px; top: 60px; width: 320px; height: 182px;
    background: var(--paper-black); border: 1px solid var(--paper-black-edge);
    padding: 34px 28px;
  }
  .cardholder { color: var(--copper); font-size: 13px; font-weight: 700; letter-spacing: 1px; }
  .job-title { color: var(--ink-grey); font-size: 8px; letter-spacing: 1.5px; margin-top: 2px; }
  .card-details { margin-top: 24px; display: grid; grid-template-columns: 1fr 1fr; gap: 6px 12px; font-size: 8px; color: #bdbdbd; }
  .card-details span { color: var(--copper); display: inline-block; width: 12px; }
  .business-card .rules { right: 26px; top: 30px; gap: 6px; }

  /* Envelopes */
  .envelope {
    left: 840px; width: 320px; height: 170px;
    background: var(--paper-black); border: 1px solid var(--paper-black-edge); overflow: hidden;
  }
  .envelope-back { top: 272px; }
  .envelope-back svg { position: absolute; inset: 0; }
  .envelope-back .brand { position: absolute; right: 34px; bottom: 30px; }
  .envelope-back .brand-name { font-size: 24px; }
  .envelope-front { top: 472px; }
  .envelope-front .brand { position: absolute; left: 28px; top: 26px; }
  .envelope-front .brand-name { font-size: 34px; }
  .envelope-front .tagline { font-size: 9px; }
  .envelope-front .rules { right: 26px; bottom: 26px; gap: 9px; }
</style>
</head>
<body>

  <section class="sheet letterhead">
    <div class="brand">
      <div class="brand-name">k7</div>
      <div class="tagline">Made to stand out.</div>
    </div>
    <div class="watermark">
      <div class="brand-name">k7</div>
      <div class="tagline">Made to stand out.</div>
    </div>
    <div class="contact">
      <div><span>✉</span>hello@k7-events.com</div>
      <div><span>⌖</span>Ateliers 12, Brussels</div>
      <div><span>☏</span>0470 12 34 56</div>
    </div>
    <div class="rules">
      <i style="width:200px"></i>
      <i style="width:150px"></i>
      <i style="width:110px"></i>
    </div>
  </section>

  <section class="sheet folder">
    <div class="brand">
      <div class="brand-name">k7</div>
      <div class="tagline">Made to stand out.</div>
    </div>
    <div class="rules">
      <i style="width:220px"></i>
      <i style="width:170px"></i>
      <i style="width:120px"></i>
    </div>
  </section>

  <section class="sheet business-card">
    <div class="cardholder">CARDHOLDER NAME</div>
    <div class="job-title">JOB TITLE</div>
    <div class="card-details">
      <div><span>◍</span>www.k7-events.com</div>
      <div><span>☏</span>0470 12 34 56</div>
      <div><span>✉</span>hello@k7-events.com</div>
      <div><span>⌖</span>Ateliers 12, Brussels</div>
    </div>
    <div class="rules">
      <i style="width:40px"></i>
      <i style="width:26px"></i>
    </div>
  </section>

  <section class="sheet envelope envelope-back">
    <svg width="320" height="170" viewBox="0 0 320 170">
      <polyline points="0,0 160,92 320,0" fill="none" stroke="#2c2c2d" stroke-width="1.5"/>
    </svg>
    <div class="brand"><div class="brand-name">k7</div></div>
  </section>

  <section class="sheet envelope envelope-front">
    <div class="brand">
      <div class="brand-name">k7</div>
      <div class="tagline">Made to stand out.</div>
    </div>
    <div class="rules">
      <i style="width:150px"></i>
      <i style="width:110px"></i>
      <i style="width:80px"></i>
    </div>
  </section>

</body>
</html>
```